Bus Card and Materials for Handyman and Landscaping
TLCard and Material
Bus Card and Materials for Handyman and Landscaping - Construction
Creative Brief
Professional
TL Handymand and Landscaping
Owner
PO Box 8172 Ridgeford, Oregon 97738
tlenz8172@mailvexa.com
Insured
I'd like to use my business card also as a magnet for my car or yard signs. I like the colors but are also open to other colors that designers use through their creativity.
One side of the card with my information the other side for marketing purposes, logo or other images, designers - please continue to use your creativity to come up with stunning designs. Thank you
TLenz TLenz
Designers! Love the designs! I'd like to list the type of work I so on the back side or on the side of the card (use your creativity, its great!): Roof Restoration Cutting Trees Roofing Yard Maintenance Painting Yard Service (weekly, bi-monthly, monthly) Pressure Washing Extensions Building Restoration Drywall & Texture Concrete Work
Welcome designers! I'm excited to view your creative cutting edge designs for my business card, stationary, car magnet, and yard signs. Good luck to you all.

```html
<!DOCTYPE html>
<html lang="en">
<head>
<meta charset="utf-8">
<title>TL Handyman and Landscaping – Business Card</title>
<link href="https://fonts.googleapis.com/css2?family=Montserrat:wght@400;600;800&display=swap" rel="stylesheet">
<style>
  :root {
    --bg: #6b6b6b;
    --green-dark: #1f7a2e;
    --green: #2f9a3a;
    --green-light: #6cc04a;
    --white: #ffffff;
    --ink: #5a5a5a;
    --ink-soft: #8a8a8a;
  }
  * { box-sizing: border-box; margin: 0; padding: 0; }
  html, body { width: 1200px; height: 876px; overflow: hidden; }
  body {
    background: var(--bg);
    font-family: "Montserrat", Arial, sans-serif;
    position: relative;
  }
  .card {
    position: absolute;
    width: 520px;
    height: 297px;
    top: 290px;
    border-radius: 6px;
    overflow: hidden;
    box-shadow: 0 10px 24px rgba(0,0,0,0.35);
  }
  /* Information side */
  .card-front { left: 50px; background: var(--white); }
  .front-edge {
    position: absolute; left: 0; top: 0; bottom: 0; width: 14px;
    background: var(--green);
  }
  .front-band {
    position: absolute; left: 0; bottom: 0; width: 190px; height: 22px;
    background: linear-gradient(90deg, var(--green-dark), var(--green-light));
  }
  .contact {
    position: absolute; left: 44px; top: 46px;
  }
  .contact-name {
    color: var(--green);
    font-weight: 800;
    font-size: 19px;
    letter-spacing: 0.5px;
    text-transform: uppercase;
  }
  .contact-role {
    color: var(--ink-soft);
    font-size: 12px;
    margin-top: 2px;
    margin-bottom: 16px;
  }
  .contact-line {
    color: var(--ink);
    font-size: 12px;
    line-height: 19px;
  }
  .front-brand {
    position: absolute; right: 36px; top: 98px;
    display: flex; align-items: center; gap: 10px;
  }
  .brand-mark {
    width: 18px; height: 18px; background: var(--green);
  }
  .front-brand .brand-name {
    color: var(--green-dark);
    font-weight: 800;
    font-size: 20px;
    line-height: 1.1;
    text-transform: uppercase;
  }
  /* Marketing side */
  .card-back {
    left: 630px;
    background: linear-gradient(135deg, var(--green-light) 0%, var(--green) 45%, var(--green-dark) 100%);
    display: flex; align-items: center; justify-content: center;
  }
  .back-brand {
    display: flex; align-items: center; gap: 14px;
  }
  .back-brand .brand-mark { width: 24px; height: 24px; background: var(--white); }
  .back-brand .brand-name {
    color: var(--white);
    font-weight: 800;
    font-size: 34px;
    line-height: 1.05;
    text-transform: uppercase;
  }
</style>
</head>
<body>
  <section class="card card-front">
    <div class="front-edge"></div>
    <div class="front-band"></div>
    <div class="contact">
      <h1 class="contact-name">TLenz Handyman</h1>
      <p class="contact-role">Owner</p>
      <p class="contact-line">PO Box 8172</p>
      <p class="contact-line">Ridgeford, Oregon 97738</p>
      <p class="contact-line">555-555-0147</p>
      <p class="contact-line">tlenz8172@mailvexa.com</p>
    </div>
    <div class="front-brand">
      <span class="brand-mark"></span>
      <span class="brand-name">TL Handyman<br>Landscaping</span>
    </div>
  </section>

  <section class="card card-back">
    <div class="back-brand">
      <span class="brand-mark"></span>
      <span class="brand-name">TL Handyman<br>Landscaping</span>
    </div>
  </section>
</body>
</html>
```